Business Card for Modern Marketing Consultancy

Business card needed for marketing consultancy with existing logo.

Lanternway Co is a specialized boutique marketing consultancy that provides startup, small and mid size consumer businesses thought leadership and implementation of marketing strategies to help your business grow.

Our expertise, experience and industry knowledge stems from some of New York’s top global beauty and retail companies and allows us to draw from an array of successful marketing strategies and growth tactics tailored to suit the needs of your business

lanternwayco.example

Target Market(s)

start up, small and mid size consumer packaged goods businesses

Industry/Entity Type

Leadership

Requirements
Must have
• Must have the logo of the business and use of the exact colors of the logo.
Must be simple, sleek, modern and clean. Must make a statement and be eye catching.

Front: looking for unique design or visual statement with logo and tagline

Back of card should have:
logo - if not use on front.
Delia R. Horvath
Founder
Lanternway Co
m: 555.014.2276
deliahorvath@lanternwayco.example
lanternwayco.example

Please use the following words as these describe my services:
strategy analytics branding research

Please refer to the website look and feel: lanternwayco.example

Please kindly note that I am looking for a unique design that I cannot do myself with a template. thank you.
Nice to have
• Please also try and incorporate additional files attached.

```html
<!DOCTYPE html>
<html lang="en">
<head>
<meta charset="utf-8">
<title>Lanternway Co — Business Card</title>
<link rel="stylesheet" href="https://fonts.googleapis.com/css2?family=Questrial&family=Montserrat:wght@600;700&display=swap">
<style>
  :root {
    --stage: #e9e6e2;
    --card-dark: #1f1f20;
    --card-mid: #2c2c2e;
    --band: #0f0f10;
    --rule: #cfcfcf;
    --logo-grey: #8c8c8c;
    --soft-grey: #b9b9b9;
    --magenta: #c2298f;
    --white: #f4f4f4;
  }
  * { box-sizing: border-box; margin: 0; padding: 0; }
  html, body {
    width: 1200px; height: 750px; overflow: hidden;
    background: var(--stage);
    font-family: "Questrial", sans-serif;
  }
  .stage {
    position: relative; width: 1200px; height: 750px;
    display: flex; align-items: center; justify-content: center; gap: 40px;
  }
  .card {
    position: relative; width: 540px; height: 309px;
    border-radius: 4px; overflow: hidden;
    box-shadow: 0 10px 28px rgba(0,0,0,.28);
  }
  .card__texture {
    position: absolute; inset: 0;
    background: radial-gradient(ellipse at 40% 40%, var(--card-mid), var(--card-dark) 75%);
  }

  /* Front */
  .front__band {
    position: absolute; left: 0; right: 0; top: 92px; height: 140px;
    background: var(--band);
    border-top: 2px solid var(--rule);
    border-bottom: 2px solid var(--rule);
    box-shadow: 0 -6px 0 -4px var(--rule), 0 6px 0 -4px var(--rule);
  }
  .front__brand {
    position: absolute; left: 46px; top: 118px;
    display: flex; align-items: center; gap: 16px;
  }
  .front__name {
    font-size: 50px; color: var(--logo-grey); letter-spacing: -0.5px; line-height: 1;
  }
  .front__dot {
    width: 44px; height: 44px; border-radius: 50%; background: var(--magenta);
  }
  .front__services {
    position: absolute; left: 48px; top: 182px;
    display: flex; align-items: center; gap: 10px;
    list-style: none;
    font-size: 13px; color: var(--soft-grey);
    letter-spacing: 2px; text-transform: uppercase;
  }
  .front__services li + li::before {
    content: ""; display: inline-block;
    width: 5px; height: 5px; border-radius: 50%;
    background: var(--magenta);
    margin-right: 10px; vertical-align: middle;
    position: relative; top: -1px;
  }

  /* Back */
  .back__mark {
    position: absolute; left: 30px; top: 98px; width: 120px;
    display: flex; flex-direction: column; align-items: center; gap: 12px;
  }
  .back__dot {
    width: 86px; height: 86px; border-radius: 50%; background: var(--magenta);
  }
  .back__mark-name { font-size: 15px; color: var(--magenta); }
  .back__panel {
    position: absolute; left: 168px; top: 26px; right: 22px; bottom: 28px;
    background: var(--band);
    border: 2px solid var(--rule); border-radius: 18px;
    padding: 22px 20px; color: var(--white);
  }
  .back__person {
    font-family: "Montserrat", sans-serif; font-weight: 700;
    font-size: 20px; letter-spacing: 1px;
  }
  .back__role { font-size: 14px; margin-top: 4px; color: #d8d8d8; }
  .back__contact {
    list-style: none; margin-top: 52px;
    font-size: 13px; line-height: 1.45; color: #e2e2e2;
  }
</style>
</head>
<body>
<main class="stage">
  <section class="card card--front" aria-label="Card front">
    <div class="card__texture" role="img" aria-label="Dark hexagonal mesh texture"></div>
    <div class="front__band"></div>
    <div class="front__brand">
      <span class="front__name">Lanternway Co</span>
      <span class="front__dot"></span>
    </div>
    <ul class="front__services">
      <li>strategy</li>
      <li>analytics</li>
      <li>branding</li>
      <li>research</li>
    </ul>
  </section>

  <section class="card card--back" aria-label="Card back">
    <div class="card__texture" role="img" aria-label="Dark hexagonal mesh texture"></div>
    <div class="back__mark">
      <span class="back__dot"></span>
      <span class="back__mark-name">Lanternway Co</span>
    </div>
    <div class="back__panel">
      <h1 class="back__person">Delia R. Horvath</h1>
      <p class="back__role">Founder</p>
      <ul class="back__contact">
        <li>Lanternway Co</li>
        <li>m: 555.014.2276</li>
        <li>deliahorvath@lanternwayco.example</li>
        <li>lanternwayco.example</li>
      </ul>
    </div>
  </section>
</main>
</body>
</html>
```